Community Legal Website

The website is about a law in legal area (Fiscal), it has a moderator and the community also contributes with information.

Attention that this is not for a Law Firm. This is a community site where all the lawyers can contribute wiith their knowledge and at the same time where they can read the Official Law in the fiscal area.

The site is in portuguese, but we have attach information in english about the functionalities.

I attach information which represents the first version of the site done by html.. That is the site we intend to improve.

The site is quite simple because the main pages are:
- Home page;
- Section page (which has the Chapters and articles)
- Article page;

This pages all belong to the article:

redaccao_actual.htm, redaccoes_anteriores.htm, anotacoes.htm, jurisprudencia.htm, decisoesadministrativas.htm, minutas.htm, duvidas.htm

AS you see in all of them the options are always there.

The most important in this site is the usability of the content:

The FAQ, Contacts, Terms of conditions, who we are, are links less important.

Also there is a possibility to have in the homepage a higligh of certain articles that we want to raise from the others.

Please check the excel sheet as well as the zip file wich has the site in portuguese that you can use a website translator to check in your language.
Updates

We added a excel sheet with the functionalities in english which the site must have.

Reason: Because this is easter time we have increased the time for the deliver

Please check briefing update.

Reason: There were some request to extend the deadline because of the Easter

Hi!

Please read carefully the briefing. People are presenting me company web sites adn this is NOT a company web site. THis is a Site wich has a content of Laws. Please check the 1st version in the zip file and improve it. The options are there and you can translate in google tradutor or reading the excel sheet attach.

txs,
JV

Reason: My client need more desing choices

Target Market(s)

Lawyers, jurists and people related with the fiscal Law.

Industry/Entity Type

Legal

Requirements
Must have
• The interface should be clean and elegant.
It should also contribute to speed.
And try to avoid to many distract elements.
The site will be dinamic and with a backoffice, so in that you have to be carefully with the space dynamic. But you don't have to worry about the backoffice. Only the front office which is the public site.

```html
<!DOCTYPE html>
<html lang="en">
<head>
<meta charset="utf-8">
<title>LEX TRIBUTA.net – Community Fiscal Law</title>
<link href="https://fonts.googleapis.com/css2?family=Open+Sans:wght@400;600;700&display=swap" rel="stylesheet">
<style>
:root{
  --ink:#1a1a1a;
  --white:#ffffff;
  --teal:#4a7a62;
  --teal-light:#5f9a80;
  --glass:rgba(70,122,96,.86);
  --news:#6e9a1c;
  --news-dark:#4d6e10;
  --row:#f0f0f0;
  --row-alt:#e0ece6;
  --footer:#343434;
  --footer-muted:#8a8a8a;
  --link-active:#6fbf9a;
}
*{box-sizing:border-box;margin:0;padding:0}
html,body{width:1200px;height:988px;overflow:hidden}
body{position:relative;background:var(--white);font-family:"Open Sans",Arial,sans-serif;color:var(--ink)}

.hero-photo{position:absolute;left:0;top:0;width:1200px;height:859px;
  background:
    linear-gradient(180deg,#3a4440 0%,#5b6a55 18%,#6f8660 32%,#5c6b58 50%,#8f8e86 68%,#b8b6ae 85%,#c9c7c0 100%);}

.brand{position:absolute;left:95px;top:8px;width:184px;height:184px;border-radius:50%;
  background:radial-gradient(circle at 45% 40%,#ffffff 60%,#e4e4e4 100%);
  box-shadow:0 2px 8px rgba(0,0,0,.45);display:flex;align-items:center;justify-content:center;z-index:2}
.brand-name{font-size:15px;font-weight:600;color:var(--teal);letter-spacing:.2px}

.main-nav{position:absolute;left:226px;top:15px;width:152px;z-index:1;list-style:none}
.main-nav li{height:28px;margin-bottom:7.8px;border-radius:0 10px 10px 0;background:#0a0a0a;
  box-shadow:0 1px 3px rgba(0,0,0,.5)}
.main-nav li.is-current{background:linear-gradient(180deg,var(--teal-light),#2f6650)}
.main-nav a{display:block;padding-left:68px;line-height:28px;color:var(--white);text-decoration:none;font-size:14.5px}

.news-bar{position:absolute;left:91px;top:486px;width:1007px;height:41px;background:var(--news);
  border-radius:6px;display:flex;align-items:center;padding-left:20px}
.news-label{color:var(--white);font-size:14.5px;margin-right:9px}
.news-text{color:#111;font-size:15px}
.news-arrows{position:absolute;right:7px;top:9px;display:flex;gap:2px}
.news-arrows span{width:23px;height:24px;background:var(--news-dark);display:flex;align-items:center;justify-content:center;border-radius:3px}

.welcome{position:absolute;left:91px;top:550px;width:483px;height:335px;background:var(--glass);
  border:1px solid rgba(255,255,255,.45);border-radius:5px;padding:14px 18px 0 18px;color:var(--white)}
.welcome h1{font-size:19px;font-weight:600;padding-bottom:4px;border-bottom:1px solid rgba(255,255,255,.55);margin-bottom:7px}
.welcome p{font-size:12.1px;line-height:18.9px;text-align:justify;margin-bottom:9.5px;hyphens:manual}

.law-panel{position:absolute;left:616px;width:482px;background:var(--row);border-radius:6px;overflow:hidden;
  box-shadow:0 0 0 1px rgba(0,0,0,.08)}
.law-panel h2{background:var(--teal);color:var(--white);font-size:21px;font-weight:400;height:46px;line-height:48px;padding-left:21px}
.law-panel ul{list-style:none}
.law-panel li{height:42px;line-height:42px;font-size:13.4px;padding-left:20px;background:var(--row)}
.law-panel li:nth-child(even){background:var(--row-alt)}
.law-panel li::before{content:"»";font-weight:700;margin-right:11px}
.fiscal{top:549px}
.administrative{top:785px;height:100px}

.site-footer{position:absolute;left:0;top:905px;width:1200px;height:83px;background:var(--footer);text-align:center}
.footer-nav{padding-top:15px;font-size:13px;color:var(--white)}
.footer-nav a{color:var(--white);text-decoration:none}
.footer-nav a.is-current{color:var(--link-active)}
.copyright{margin-top:7px;font-size:11px;color:var(--footer-muted)}
</style>
</head>
<body>

<div class="hero-photo" role="img" aria-label="Group photo of community members standing outdoors in front of a building with green shrubs"></div>

<div class="brand"><span class="brand-name">LEX TRIBUTA.net</span></div>

<ul class="main-nav">
  <li class="is-current"><a href="#">HOME</a></li>
  <li><a href="#">ABOUT</a></li>
  <li><a href="#">SECTION</a></li>
  <li><a href="#">ARTICLE</a></li>
  <li><a href="#">CONTACTS</a></li>
</ul>

<div class="news-bar">
  <span class="news-label">LATEST NEWS :</span>
  <span class="news-text">Lorem ipsum dolor sit amet, consectetur adipiscing elit. Suspendisse tincidunt sapien at elit</span>
  <div class="news-arrows">
    <span><svg width="9" height="11" viewBox="0 0 9 11"><path d="M8 0 L0 5.5 L8 11Z" fill="#000"/></svg></span>
    <span><svg width="9" height="11" viewBox="0 0 9 11"><path d="M1 0 L9 5.5 L1 11Z" fill="#000"/></svg></span>
  </div>
</div>

<section class="welcome">
  <h1>Welcome to LEX TRIBUTA.net!</h1>
  <p>Lorem ipsum dolor sit amet, consectetur adipiscing elit. Etiam porta mollis tortor, nec mollis purus rhoncus eget. Nunc justo tellus, malesuada vitae malesuada eu, condimentum vel erat. Morbi sollicitudin erat vitae sapien dictum varius a sit amet massa.</p>
  <p>Donec quis erat ac eros placerat blandit convallis eu ipsum. Nulla facilisi. Praesent quis eros posuere erat rutrum pharetra eu nec neque. Pellen&shy;tesque a justo nulla, ut molestie felis. Vestibulum bibendum suscipit mattis.</p>
  <p>Quisque in nulla eget magna auctor iaculis. Duis pulvinar facilisis fermen&shy;tum. Integer a vulputate nisi. Proin sit amet orci erat, eu rutrum lacus.</p>
  <p>Lorem ipsum dolor sit amet, consectetur adipiscing elit. Etiam porta mollis tortor, nec mollis purus rhoncus eget. Nunc justo tellus, malesuada vitae malesuada eu, condimentum vel erat. ut molestie felis. Vestibulum</p>
</section>

<section class="law-panel fiscal">
  <h2>LEGISLATION FISCAL ANNOTATED</h2>
  <ul>
    <li>IRS Code - Income Tax of Individuals</li>
    <li>IRC Code - Tax Income Tax</li>
    <li>IMI Code - Property Tax</li>
    <li>RCPIT - Supplementary Rules of Procedure of the Tax Inspectorate</li>
  </ul>
</section>

<section class="law-panel administrative">
  <h2>ADMINISTRATIVE LAW ANNOTATED</h2>
  <ul>
    <li>CPTA - Code of Administrative Court Procedure</li>
  </ul>
</section>

<footer class="site-footer">
  <nav class="footer-nav">
    <a href="#" class="is-current">Home</a> | <a href="#">About</a> | <a href="#">Section</a> | <a href="#">Article</a> | <a href="#">Contacts</a> | <a href="#">Terms of Use</a> | <a href="#">FAQ</a> | <a href="#">About Us</a> | <a href="#">Contacts</a>
  </nav>
  <p class="copyright">Copyright © 2013 LEX TRIBUTA.net &nbsp;All rights reserved.</p>
</footer>

</body>
</html>
```